Private Investment Firm Needs PowerPoint Presentation Template

Design PowerPoint template, take Ridgeholm-submitted rough presentation draft, and drop it into new template. See attached Project Brief file for more detail.
Updates

Some decent designs have been submitted but they seem to lack the understanding of our target markets. I am hopeful that more time and feedback will result in better results.

Target Market(s)

Private company owners and intermediaries.

Font styles to use
Serif

Colors
3176b5

Requirements
Must have
• See attached Project Brief.
Nice to have
Should not have
• No B2C fluff--this is a B2B project.

```html
<!DOCTYPE html>
<html lang="en">
<head>
<meta charset="utf-8">
<title>Investment Criteria – Ridgeholm</title>
<link href="https://fonts.googleapis.com/css2?family=Figtree:wght@400;600;700&family=Tinos&display=swap" rel="stylesheet">
<style>
  :root {
    --brand-blue: #0070c0;
    --title-blue: #0a6ec4;
    --ink-grey: #555555;
    --page-bg: #ffffff;
    --text-on-blue: #ffffff;
  }
  * { margin: 0; padding: 0; box-sizing: border-box; }
  html, body { width: 1200px; height: 676px; overflow: hidden; background: var(--page-bg); }
  .slide {
    position: relative;
    width: 1200px;
    height: 676px;
    overflow: hidden;
    background: var(--page-bg);
    font-family: "Figtree", sans-serif;
  }
  .side-rail {
    position: absolute; left: 0; top: 0;
    width: 44px; height: 676px;
    background: var(--brand-blue);
  }
  .side-rail-url {
    position: absolute;
    left: 22px; top: 336px;
    transform: translate(-50%, -50%) rotate(-90deg);
    white-space: nowrap;
    font-family: "Tinos", serif;
    font-size: 14px;
    color: var(--text-on-blue);
    letter-spacing: 0.3px;
  }
  .edge-rail {
    position: absolute; right: 0; top: 0;
    width: 12px; height: 676px;
    background: var(--brand-blue);
  }
  .page-number {
    position: absolute; right: 22px; top: 18px;
    font-family: "Tinos", serif;
    font-size: 19px;
    color: #222;
  }
  .slide-title {
    position: absolute; left: 86px; top: 80px;
    font-size: 29px; font-weight: 700;
    letter-spacing: 0.4px;
    color: var(--title-blue);
  }
  .headline {
    position: absolute; right: 748px; top: 224px;
    text-align: right;
    font-size: 42px; font-weight: 700;
    line-height: 42px;
    color: var(--ink-grey);
  }
  .headline .accent { color: var(--title-blue); }
  .criteria-panel {
    position: absolute; left: 482px; top: 170px;
    width: 706px; height: 334px;
    background: var(--brand-blue);
  }
  .criteria-list {
    list-style: none;
    position: absolute; left: 42px; top: 40px;
  }
  .criteria-list li {
    display: flex; align-items: center;
    height: 37.6px;
    font-size: 17.6px;
    color: var(--text-on-blue);
  }
  .criteria-list li::before {
    content: "";
    width: 10px; height: 10px;
    margin-right: 10px;
    background: var(--text-on-blue);
    flex-shrink: 0;
  }
  .architecture-photo {
    position: absolute; left: 470px; top: 504px;
    width: 718px; height: 172px;
    background: linear-gradient(100deg, #ffffff 0%, #f2f4f4 35%, #dfe5e5 70%, #c9d3d2 100%);
  }
  .brand-mark {
    position: absolute; left: 68px; top: 616px;
    display: flex; align-items: center; gap: 10px;
  }
  .brand-mark-dot {
    width: 34px; height: 34px; border-radius: 50%;
    background: var(--brand-blue);
  }
  .brand-mark-name {
    font-size: 20px; font-weight: 700;
    letter-spacing: 1.5px;
    color: var(--brand-blue);
  }
</style>
</head>
<body>
<div class="slide">
  <div class="side-rail"><span class="side-rail-url">www.ridgeholmcapital.com</span></div>
  <div class="edge-rail"></div>
  <div class="page-number">18</div>

  <h1 class="slide-title">INVESTMENT CRITERIA</h1>

  <p class="headline">
    <span class="accent">Ridgeholm invests</span><br>
    in established,<br>
    lower middle<br>
    market<br>
    companies.
  </p>

  <section class="criteria-panel">
    <ul class="criteria-list">
      <li>Revenues of $10MM to $150MM</li>
      <li>EBITDA of at least $2MM</li>
      <li>Ridgeholm investment size of $5MM to $25MM</li>
      <li>Experienced, committed, and incented management</li>
      <li>Limited leverage (aka debt) “ahead” of Ridgeholm</li>
      <li>Niche market leader with differentiated services or products</li>
      <li>Focused on value-added execution, not proof of concept</li>
    </ul>
  </section>

  <div class="architecture-photo" role="img" aria-label="Photo of a modern white building facade with curved vertical fins"></div>

  <div class="brand-mark">
    <span class="brand-mark-dot"></span>
    <span class="brand-mark-name">RIDGEHOLM</span>
  </div>
</div>
</body>
</html>
```